KVT Business Cards

We require business cards for our business. We would like a matte black back to the card, with our logo centred in the middle. The front side of the card is open to design.

Target Market(s)

Clients looking for legal services (professional)

Industry/Entity Type

Legal

Contact Information for Business Card

Boris Telemark
Partner
Mobile: 0438 715 642
Email: boris@kvtlaw.co
Website: www.kvtlaw.co
Level 3, 118 Wexbury Street
Sydney NSW 2000

Font styles to use
Other font styles liked:
• Avenir

Colors
f04a50
ffffff
1b1b1b

Requirements
Must have
• Black back with logo included in the centre of the card.
• Our font is Avenir.

```html
<!DOCTYPE html>
<html lang="en">
<head>
<meta charset="utf-8">
<title>KVT Business Cards</title>
<link rel="stylesheet" href="https://fonts.googleapis.com/css2?family=Nunito+Sans:wght@300;400;600&display=swap">
<style>
  :root {
    --ink: #1b1b1b;
    --card: #141414;
    --accent: #f04a50;
    --edge: #b0173f;
    --paper: #ffffff;
    --ground: #e9e9ea;
  }
  * { margin: 0; padding: 0; box-sizing: border-box; }
  html, body { width: 1200px; height: 800px; overflow: hidden; }
  body {
    background: var(--ground);
    font-family: "Nunito Sans", "Avenir", sans-serif;
    position: relative;
  }
  .card {
    position: absolute;
    top: 235px;
    width: 540px;
    height: 330px;
    background: var(--card);
    border-bottom: 4px solid var(--edge);
  }
  .card--back { left: 40px; }
  .card--front { left: 620px; }
  .card--front::after {
    content: "";
    position: absolute;
    inset: 8px;
    border: 1px solid rgba(240, 74, 80, 0.35);
    pointer-events: none;
  }

  .brand {
    position: absolute;
    display: flex;
    align-items: center;
    gap: 18px;
  }
  .brand__mark {
    background: var(--accent);
    flex: none;
  }
  .brand__name {
    color: var(--paper);
    font-weight: 600;
    text-transform: uppercase;
    line-height: 1.05;
    letter-spacing: 0.02em;
  }
  .card--back .brand { left: 50%; top: 50%; transform: translate(-50%, -50%); }
  .card--back .brand__mark { width: 58px; height: 58px; }
  .card--back .brand__name { font-size: 27px; }

  .card--front .brand { left: 48px; top: 168px; gap: 14px; }
  .card--front .brand__mark { width: 44px; height: 44px; }
  .card--front .brand__name { font-size: 20px; }

  .contact {
    position: absolute;
    left: 292px;
    top: 62px;
    color: var(--paper);
  }
  .contact__name {
    font-size: 23px;
    font-weight: 300;
    text-transform: uppercase;
    letter-spacing: 0.03em;
  }
  .contact__role {
    font-size: 15px;
    color: var(--accent);
    text-transform: uppercase;
    letter-spacing: 0.05em;
    margin-bottom: 16px;
  }
  .contact__list { list-style: none; font-size: 14px; font-weight: 400; }
  .contact__item {
    display: flex;
    align-items: center;
    gap: 9px;
    margin-bottom: 7px;
  }
  .contact__icon { width: 12px; height: 12px; flex: none; }
  .contact__address {
    font-size: 14px;
    line-height: 1.55;
    margin-top: 8px;
    font-style: normal;
  }
</style>
</head>
<body>

  <section class="card card--back" aria-label="Card back">
    <div class="brand">
      <span class="brand__mark"></span>
      <span class="brand__name">Kestrel Vale<br>Telemark<br>Legal</span>
    </div>
  </section>

  <section class="card card--front" aria-label="Card front">
    <div class="brand">
      <span class="brand__mark"></span>
      <span class="brand__name">Kestrel Vale<br>Telemark<br>Legal</span>
    </div>

    <div class="contact">
      <h1 class="contact__name">Boris Telemark</h1>
      <p class="contact__role">Partner</p>
      <ul class="contact__list">
        <li class="contact__item">
          <svg class="contact__icon" viewBox="0 0 12 12" aria-hidden="true"><rect x="3" y="0.5" width="6" height="11" rx="1" fill="none" stroke="#f04a50" stroke-width="1.2"/><circle cx="6" cy="9.5" r="0.7" fill="#f04a50"/></svg>
          0438 715 642
        </li>
        <li class="contact__item">
          <svg class="contact__icon" viewBox="0 0 12 12" aria-hidden="true"><rect x="0.5" y="2.5" width="11" height="7" fill="#f04a50"/><path d="M0.5 2.5 L6 6.5 L11.5 2.5" fill="none" stroke="#141414" stroke-width="1"/></svg>
          boris@kvtlaw.co
        </li>
        <li class="contact__item">
          <svg class="contact__icon" viewBox="0 0 12 12" aria-hidden="true"><circle cx="6" cy="6" r="5.2" fill="none" stroke="#f04a50" stroke-width="1.1"/><ellipse cx="6" cy="6" rx="2.2" ry="5.2" fill="none" stroke="#f04a50" stroke-width="1"/><line x1="0.8" y1="6" x2="11.2" y2="6" stroke="#f04a50" stroke-width="1"/></svg>
          www.kvtlaw.co
        </li>
      </ul>
      <address class="contact__address">Level 3, 118 Wexbury Street<br>Sydney NSW 2000</address>
    </div>
  </section>

</body>
</html>
```